Broschüre für Toben – Balgen – Kraftprobe
Zielgruppe
Wir bieten Rangel und Raufkurse für Kinder ab dem Vorschulalter bis zu weiterführenden Schulen. Die Broschüre erhalten Lehrer, Erzieher und Direktoren der Einrichtungen an denen die Kurse Angeboten werden.
Aufgabenstellung
Design sollte eher Schlicht und modern wirken und an der homepage
www.boden-lernwerk.de orientiert sein.
Infobroschüre zum Durchblättern, kein Folder. Seitenfolge wie auf der Powerpoint präsentation.

```html
<!DOCTYPE html>
<html lang="de">
<head>
<meta charset="utf-8">
<title>Broschüre – Toben – Balgen – Kraftprobe</title>
<link href="https://fonts.googleapis.com/css2?family=Open+Sans:ital,wght@0,400;0,600;0,700;1,400;1,600&family=Roboto+Condensed:ital,wght@0,700;1,700&display=swap" rel="stylesheet">
<style>
:root{
  --bg:#e7e7e9;
  --paper:#f8f8f8;
  --paper-edge:#e2e2e4;
  --red:#c81f27;
  --ink:#5e5e5e;
  --ink-dark:#3b3b3b;
  --panel:#e9e9eb;
}
*{box-sizing:border-box;margin:0;padding:0}
html,body{width:1200px;height:3352px;overflow:hidden;background:var(--bg)}
body{position:relative;font-family:"Open Sans",Arial,sans-serif;color:var(--ink)}
.spread{position:absolute;width:614px;height:318px;display:flex;box-shadow:0 4px 14px rgba(0,0,0,.12)}
.page{position:relative;width:307px;height:100%;background:var(--paper);overflow:hidden}
.page.left{border-right:1px solid var(--paper-edge);background:linear-gradient(90deg,var(--paper) 88%,#ececee)}
.page.right{background:linear-gradient(90deg,#ececee,var(--paper) 12%)}
.content{position:absolute;inset:22px 22px 16px 28px}
.heading{display:inline-block;background:var(--red);color:#fff;font-family:"Roboto Condensed",Arial Narrow,sans-serif;font-weight:700;font-size:9.5px;line-height:1.25;padding:2px 5px;text-transform:uppercase;letter-spacing:.2px}
.heading-stack .heading{display:table;margin-bottom:2px}
.tag{display:inline-block;background:var(--red);color:#fff;font-family:"Roboto Condensed",Arial Narrow,sans-serif;font-style:italic;font-weight:700;font-size:6.2px;line-height:1.3;padding:1px 4px;text-transform:uppercase;margin:6px 0 3px}
.tag.grey{background:var(--panel);color:var(--ink-dark)}
.copy{font-size:5.6px;line-height:1.5;text-align:justify;margin-bottom:6px}
.photo{position:absolute}
.ticks{list-style:none}
.ticks li{position:relative;padding-left:7px;font-size:5.4px;line-height:1.45;font-style:italic;color:var(--red);margin-bottom:4px}
.ticks li svg{position:absolute;left:0;top:1px}
.unit{margin-bottom:7px}
.unit b{display:block;font-size:6px;color:var(--red);font-weight:700}
.unit span{font-size:5.6px}
.offer{background:var(--panel);padding:6px 8px;margin:6px 0}
.offer h3{font-family:"Roboto Condensed",Arial Narrow,sans-serif;font-style:italic;font-weight:700;color:var(--red);font-size:9px;line-height:1.2}
.offer p{font-size:5.4px;font-weight:600;color:var(--ink-dark);line-height:1.4;margin-top:2px}
.callout{position:absolute;background:var(--red);color:#fff;font-size:5.2px;font-style:italic;line-height:1.45;padding:6px}
.person{position:absolute;width:110px}
.person h4{font-size:6px;font-weight:700;color:var(--ink-dark);text-transform:uppercase}
.person p{font-size:5px;line-height:1.4;font-style:italic}
.person q{display:block;font-size:5px;line-height:1.4;font-style:italic;color:var(--red);margin-top:5px}
.voice{font-size:5.4px;line-height:1.5;font-style:italic;margin-bottom:6px;text-align:justify}
.voice b{display:block;font-style:normal;color:var(--ink-dark);font-size:5.4px}
</style>
</head>
<body>

<section class="spread" style="left:141px;top:204px">
  <div class="page left">
    <div class="photo" role="img" aria-label="Foto: zwei Jungen stehen sich Stirn an Stirn gegenüber" style="left:44px;top:18px;width:252px;height:282px;background:linear-gradient(135deg,#8aa06a,#c9a68c 45%,#5b6f8e)"></div>
  </div>
  <div class="page right">
    <div class="content" style="inset:16px 42px 16px 14px">
      <div class="heading-stack"><span class="heading">Rangeln und Raufen ist eine Urform</span><span class="heading">der kindlichen Bewegung</span></div>
      <div style="margin-top:26px">
        <p class="copy">In der heutigen Zeit scheint es Eltern und Erziehungspersonen schwer zu fallen, den richtigen Mittelweg für die Erziehung zu finden. Lässt man Kindern freien Lauf, machen sie oft, was sie wollen. Sie raufen, streiten und rebellieren. Doch ist der richtige Weg, dieses Verhalten bedingungslos zu unterbinden? Schließlich sind es Verhaltensweisen, die Kinder gerade dann ausprägen, wenn sie sich unbeschwert bewegen dürfen.</p>
        <p class="copy">Rangeln und Raufen liegt in der menschlichen Natur. Es ist eine Urform der kindlichen Bewegung. Streit ist ein soziales Phänomen, das überall existiert und nicht zu vermeiden ist. Kinder, die auch mal rebellisch sind, entwickeln sich zu selbstständigen Menschen, die ihren persönlichen Weg finden.</p>
        <p class="copy">Es ist unsere tiefe Überzeugung, dass unser Kampfsport diese kindlichen Eigenschaften in eine gesunde Richtung lenken kann. Kinder lernen spielerisch und friedlich miteinander zu raufen und ihre eigenen Grenzen zu entdecken. Sie erfahren die Kräfte ihres Körpers und erleben Respekt, Selbstdisziplin und Teamgeist.</p>
      </div>
    </div>
  </div>
</section>

<section class="spread" style="left:439px;top:605px">
  <div class="page left">
    <div class="content" style="inset:16px 14px 16px 40px">
      <div class="heading-stack"><span class="heading">Friedliches Rangeln und Raufen zur</span><span class="heading">Entwicklungsförderung</span></div>
      <div style="margin-top:20px">
        <p class="copy">Sich fit fühlen, sich etwas zutrauen und ein gesundes Selbstbewusstsein entwickeln – das sind positive Vorzüge von sportlichen Angeboten für Kinder und Jugendliche. Gerade bei jungen Menschen sollte der Spaß an der Bewegung gefördert werden, was dazu beiträgt, Sport zu einem selbstverständlichen Teil ihres Lebens zu machen.</p>
        <p class="copy">Unser Konzept basiert auf einem modernen Kampfsport, der Bodenkampf zu Hilfe nimmt und statt Schlägen und Tritten auf das Einsetzen des eigenen Körpergewichts setzt, um den Gegenüber am Boden zu kontrollieren. „Toben, Balgen und Kraftprobe“ stellt die Urform der kindlichen Bewegung dar. Mit diesem Spielfeld in einem sicheren und friedvollen Rahmen wird eine der besten Voraussetzungen für eine optimale körperliche und geistige Entwicklung geschaffen. Kinder lernen sich gegenseitig zu achten und ihre Kräfte zu messen, ohne andere zu verletzen.</p>
        <p class="copy">Gerade aufgeweckte und im Unterricht unruhige Kinder finden ihren Platz gerne auf der Matte, wo sie sich messen und ihren Überschuss an Energie loswerden dürfen. Die Kinder erhalten Anerkennung, die sie möglicherweise in anderen Bereichen nicht bekommen, und haben durch den Sport die Chance, über sich hinauszuwachsen.</p>
      </div>
    </div>
  </div>
  <div class="page right">
    <div class="content" style="inset:26px 40px 16px 24px">
      <p class="copy">Steigerung des Selbstbewusstseins. Zusammen mit verbalen Strategen zur Konfliktlösung kann bereits im Vorfeld verhindert werden, dass Kinder in eine Opferrolle hineingeraten.</p>
      <p class="copy">Rangeln und friedliches Raufen wird in der modernen Erziehung bereits als bedeutungsvolles pädagogisches Medium erkannt. An der Umsetzung scheitert es jedoch meistens, da Erzieher und Lehrer ohne eigene Kampfsporterfahrungen oder spezielle Ausbildung zu großen Respekt vor dieser Thematik haben. Im Gegensatz dazu fehlt Kampfsportlern die Feinfühligkeit, dieses Thema kindgerecht zu vermitteln. Wir verbinden pädagogische Ausbildung mit langjähriger Erfahrung als aktive Wettkämpfer und Trainer im Kinder- und Jugendbereich.</p>
      <span class="tag">Toben – Balgen – Kraftprobe</span><br>
      <span class="tag grey" style="margin-top:0">Brazilian Jiu-Jitsu zur Entwicklungsförderung</span><br>
      <span class="tag" style="margin-top:10px">Mutige Kinder - Mutige Zukunft</span><br>
      <span class="tag grey" style="margin-top:0">Stärkentraining für einen sicheren Schulstart</span>
    </div>
  </div>
</section>

<section class="spread" style="left:141px;top:1006px">
  <div class="page left">
    <div class="content" style="inset:30px 14px 16px 44px">
      <span class="heading">Toben – Balgen – Kraftprobe</span>
      <div style="margin-top:26px">
        <p class="copy">Das zentrale Ziel des Programms ist es, den Kindern wichtige Kompetenzen zu vermitteln, die notwendig sind, um friedlich und ohne Anleitung miteinander zu kämpfen. Dies stellt eine hohe emotionale Herausforderung dar und kann nur erfolgen, wenn klare Regeln vereinbart und eingehalten werden. Um dies zu gewährleisten, dass das Training verletzungsfrei für alle abläuft, teilen wir die Unterrichtsstunde in mehrere Phasen.</p>
        <span class="tag">Phase 1: Kennen lernen und Vertrauen aufbauen</span>
        <p class="copy">Der Prozess zum Aufbau eines vertrauensvollen Verhältnisses benötigt viel Zeit und pädagogisches Feingefühl. Je nachdem, wie gut die Teilnehmer bereits untereinander bekannt sind und wie stark die Heterogenität der Gruppe ausfällt, kann das Kennenlernen im Stehen stattfinden.</p>
        <span class="tag">Phase 2: Erarbeiten der Regeln, Aufbau von Körperkontakt<br>und allgemeines Aufwärmen</span>
        <p class="copy">Bereits zum Aufwärmen werden klare Regeln festgelegt. Dadurch soll den Teilnehmern verdeutlicht werden, wie wichtig die Einhaltung von Regeln allgemein und vor allem später beim Kämpfen ist. Wir nutzen verschiedene Spiele, um einen Körperkontakt aufzubauen und um zu lernen, miteinander zu tun zu haben.</p>
      </div>
    </div>
  </div>
  <div class="page right">
    <div class="photo" role="img" aria-label="Foto: Kinder beim Tauziehen auf einer Wiese" style="left:6px;top:18px;width:258px;height:282px;background:linear-gradient(160deg,#d9e3c4,#8bb35a 45%,#3c8f4a 70%,#2d5d8c)"></div>
  </div>
</section>

<section class="spread" style="left:424px;top:1429px">
  <div class="page left">
    <div class="content" style="inset:72px 14px 16px 48px">
      <span class="tag">Phase 3: Technikteil</span>
      <p class="copy">Einfache Basistechniken aus dem Brazilian Jiu-Jitsu reichen aus, um den Gegenüber am Boden zu kontrollieren, ohne ihm dabei wehzutun. Die Kinder dürfen das Gezeigte partnerweise trainieren und ausprobieren. Dabei wird der Unterschied zwischen „Miteinander“ und friedlichem „Gegeneinander“ betont. Erfolgserlebnisse und vertrauensvolles Miteinander stärken das Selbstbewusstsein.</p>
      <span class="tag">Phase 4: Rangel und Raufspiele</span>
      <p class="copy">Als Vorstufe zum freien Kämpfen dürfen die Teilnehmer nun erstmals vom „Miteinander“ ins spielerische „Gegeneinander“ übergehen. Wichtige Regeln werden nochmals wiederholt, bevor unter Anleitung verschiedene Positionen am Boden oder auch im Stand ausgekämpft werden dürfen.</p>
      <span class="tag">Phase 5: Freies Kämpfen</span>
      <p class="copy">Wenn deutlich wird, dass die Teilnehmer das Rangeln und Raufen in Phase 4 emotional gut verkraften, dürfen sie unangeleitet – also ohne Vorgabe einer Aufgabenstellung – frei kämpfen. Das freie Kämpfen dient als Messlatte und zeigt, inwieweit die pädagogischen Ziele erreicht wurden.</p>
    </div>
  </div>
  <div class="page right">
    <div class="content" style="inset:70px 34px 16px 22px">
      <ul class="ticks">
        <li><svg width="5" height="5" viewBox="0 0 10 10"><path d="M1 5l3 3 5-7" stroke="#c81f27" stroke-width="2" fill="none"/></svg>Die Kinder entwickeln eine kampfspezifische Fürsorge und achten auf die Gesundheit ihres Partners</li>
        <li><svg width="5" height="5" viewBox="0 0 10 10"><path d="M1 5l3 3 5-7" stroke="#c81f27" stroke-width="2" fill="none"/></svg>Unterlegene Kinder lernen sich strategisch aus misslichen Lagen zu befreien. Damit sind sie auch in Stresssituationen ruhig zu bleiben</li>
        <li><svg width="5" height="5" viewBox="0 0 10 10"><path d="M1 5l3 3 5-7" stroke="#c81f27" stroke-width="2" fill="none"/></svg>Die Kinder erfahren unmittelbar, dass kritische Situationen und Konflikte durch ruhig durchdachte Strategien gelöst werden können und vor allem, dass aggressives Verhalten keinesfalls die beste Lösung darstellt</li>
        <li><svg width="5" height="5" viewBox="0 0 10 10"><path d="M1 5l3 3 5-7" stroke="#c81f27" stroke-width="2" fill="none"/></svg>Wenn Regeln vereinbart werden, müssen sie eingehalten werden. Die Kinder lernen, dass man respektvoll behandelt wird, wenn man anderen im Gegenzug auch respektvoll gegenübertritt</li>
        <li><svg width="5" height="5" viewBox="0 0 10 10"><path d="M1 5l3 3 5-7" stroke="#c81f27" stroke-width="2" fill="none"/></svg>Durch das Rangeln und Raufen lernen die Kinder ihren Körper wahrzunehmen. Sie erfahren am eigenen Leib, welche Auswirkungen Handlungen auf andere haben können</li>
        <li><svg width="5" height="5" viewBox="0 0 10 10"><path d="M1 5l3 3 5-7" stroke="#c81f27" stroke-width="2" fill="none"/></svg>Die Kinder erhalten ein realistisches Selbstbild. Sie lernen zu sehen, wo ihre Stärken und Schwächen liegen</li>
      </ul>
      <span class="tag">Phase 6: Auflockerung und Verarbeitung des Erlebten durch<br>Meditationsphase oder Abschlussspiele</span>
      <p class="copy">Ein Abschlussspiel ohne kampfbetonte Aspekte soll die Stunde vom Gegeneinander wieder zum Miteinander zurückführen und ein spaßiges Ende für alle gewährleisten.</p>
    </div>
  </div>
</section>

<section class="spread" style="left:133px;top:1853px">
  <div class="page left">
    <div class="photo" role="img" aria-label="Foto: Mädchen mit Schulranzen im Schulflur, im Hintergrund weitere Kinder" style="left:44px;top:20px;width:252px;height:280px;background:linear-gradient(120deg,#e9dcc4,#cfae7a 40%,#9a8a78 70%,#4f6c82)"></div>
  </div>
  <div class="page right">
    <div class="content" style="inset:18px 24px 16px 14px">
      <span class="heading">Mutige Kinder - Mutige Zukunft</span>
      <div style="margin-top:22px">
        <span class="tag">Wir stärken Kinder auf ihrem Weg ins Schulleben</span>
        <p class="copy">Selbstsicherheit und souveränes Auftreten sind die wichtigsten Bausteine, nicht nur für einen gelingenden Schulstart, sondern auch für eine erfolgreiche Zukunft. Dabei ist es wichtig, Kinder auf Gefahren aufmerksam zu machen – ohne sie dabei zu verängstigen. Wir zeigen ihnen im Kurs Mittel und Möglichkeiten, wie sie Belastungssituationen sicher und souverän bewältigen können.</p>
        <span class="tag">Bei den zentralen Themen unseres Kurses erstrecken sich dabei über<br>4 Einheiten je 45 Minuten</span>
        <div style="margin-top:6px">
          <div class="unit"><b>1. EINHEIT</b><span>Wie gehe ich selbstsicher mit neuen Mitschülern um und wie finde ich neue Freunde?</span></div>
          <div class="unit"><b>2. EINHEIT</b><span>Wie verhalte ich mich souverän in Streitsituationen?</span></div>
          <div class="unit"><b>3. EINHEIT</b><span>Wie verhalte ich mich auf dem Schulweg und wie komme ich sicher nach Hause?</span></div>
          <div class="unit"><b>4. EINHEIT</b><span>Wie gehe ich mit Erfolgserlebnissen um und wie reagiere ich auf Rückschläge?</span></div>
        </div>
      </div>
    </div>
  </div>
</section>

<section class="spread" style="left:430px;top:2280px">
  <div class="page left">
    <div class="photo" role="img" aria-label="Foto: Mädchen sitzt zusammengekauert an einer Wand" style="left:50px;top:20px;width:246px;height:280px;background:linear-gradient(150deg,#d8d3cd,#bcb2a6 50%,#8f8478)"></div>
    <div class="callout" style="left:48px;top:195px;width:104px">
      <p>Im Umgang mit Kindern ist es uns sehr wichtig, die Inhalte spielerisch und unbeschwert zu vermitteln. Die verbalen und körperlichen Abwehrstrategien werden durch Rollenspiele gefestigt.</p>
      <p style="margin-top:5px">Speziell konzipierte Rangel- und Raufspiele vermitteln eine emotionale Umsetzung der Inhalte und garantieren Spaß für alle teilnehmenden Kinder.</p>
    </div>
  </div>
  <div class="page right">
    <div class="content" style="inset:20px 24px 16px 14px">
      <span class="heading">Kursangebot</span>
      <div style="margin-top:22px">
        <div class="offer">
          <h3>Toben – Balgen – Kraftprobe</h3>
          <p>KINDERGÄRTEN | SCHULEN | SONSTIGE PÄDAGOGISCHE EINRICHTUNGEN (KINDER- UND JUGENDHEIM ETC.)</p>
        </div>
        <p class="copy">Gruppengröße und zeitlicher Rahmen des Kurses „Toben – Balgen – Kraftprobe“ wird in Absprache mit dem pädagogischen Personal vor Ort bestimmt. Schwerpunkte können in den Bereichen der Mobbing- und Gewaltprävention, im Antiaggressionstraining oder der Jungen- und Mädchenarbeit gesetzt werden.</p>
        <div class="offer" style="margin-top:10px">
          <h3>Stärkentraining – Mutige Kinder –<br>mutige Zukunft</h3>
          <p>KINDERGÄRTEN (4 X 45 MIN, MAX. 20 TEILNEHMER)<br>GRUNDSCHULEN BIS EINSCHLIESSLICH 5. KLASSE<br>(4 X 45 MIN, 20-30 TEILNEHMER)</p>
        </div>
      </div>
    </div>
  </div>
</section>

<section class="spread" style="left:118px;top:2710px">
  <div class="page left">
    <div class="content" style="inset:32px 14px 16px 48px">
      <span class="heading">Über uns</span>
    </div>
    <div class="photo" role="img" aria-label="Foto: die beiden Trainer in schwarzen T-Shirts" style="left:100px;top:62px;width:160px;height:100px;background:linear-gradient(180deg,var(--paper) 0%,#6b6b6b 55%,#1f1f1f)"></div>
    <div style="position:absolute;left:48px;top:166px;width:250px;height:2px;background:var(--red)"></div>
    <div class="person" style="left:52px;top:176px">
      <h4>Jonas Brandt</h4>
      <p>Bachelor of Arts Pädagogik/Sportdidaktik<br>Universität Lindenfeld</p>
      <q>„Wenn Kinder friedlich miteinander rangeln und raufen können, lernen sie Grenzen zu achten und Konflikte gewaltfrei zu lösen.“</q>
    </div>
    <div class="person" style="left:182px;top:176px">
      <h4>Lukas Fehrmann</h4>
      <p>Bachelor of Arts Pädagogik<br>Universität Lindenfeld</p>
      <q>„Unser Ansatz verbindet Kampfsport mit Pädagogik und gibt Kindern Raum, über sich hinauszuwachsen.“</q>
    </div>
  </div>
  <div class="page right">
    <div class="content" style="inset:32px 40px 16px 12px">
      <span class="heading">Lehrerstimmen</span>
      <div style="margin-top:20px">
        <span class="tag">Wir legen viel Wert auf einen stetigen Austausch<br>mit den anwesenden Lehrkräften</span>
        <p class="voice"><b>REALSCHULE AUENTAL</b>Die Kinder waren mit viel Freude und Engagement dabei. Besonders positiv war, dass auch ruhigere Schüler ihren Platz gefunden und Selbstvertrauen gewonnen haben.</p>
        <p class="voice"><b>SABINE OSTERMANN (GRUNDSCHULE WEIDENBACH)</b>Die Trainer haben es verstanden, mit den Schülern auf Augenhöhe zu arbeiten. Regeln wurden klar vermittelt und konsequent eingehalten. Die Klassengemeinschaft hat spürbar profitiert.</p>
        <p class="voice">Eine tolle Erfahrung für unsere Kinder, die wir gerne wiederholen möchten.</p>
        <p class="voice"><b>RAINER HOLM | PETRA LINDNER (MITTELSCHULE AUENTAL)</b>Gerade unruhige Schülerinnen und Schüler konnten durch kontrollierte Kämpfe ihre Energie sinnvoll einsetzen. Teamfähigkeit und gegenseitiger Respekt wurden deutlich gestärkt.</p>
      </div>
    </div>
  </div>
</section>

</body>
</html>
```